Etiketten-Design für familiengeführten Weinbaubetrieb
Zielgruppe
Wir sind ein Familiengeführter Weinbaubetrieb und vermarkten unseren Wein in 0,75l Flaschen sowie auch Säfte und Schnäpse.
Zur zeit Verkaufen wir unseren Wein an Gastro und Private Kunden auch teils über Messen
Aufgabenstellung
Das derzeitige Etikett ist recht schlicht gestaltet und das Logo besteht rein aus dem geschriebenen Namen Winzerhof Dolmeck. Es kann aber auch gerne nur mit dem Namen Dolmeck ohne Winzerhof gearbeitet werden! Mit dem einbringen einer neuen Generation in den Betrieb wollen wir das aussehen unserer Produkte erneuern. Dazu kann sich gerne mit dem Namen als 'Logo' in jeglicher Art gespielt werden. Wir füllen unsere Weine in 0,75l Bordeaux Flaschen. Die Form des Etikett ist kein K.O. Kriterium jedoch wurde ursprünglich ein rund um Etikett angedacht. Sollten die Designes sich auch anders realisieren lassen sind wir gerne offen für Ideen.

```html
<!DOCTYPE html>
<html lang="de">
<head>
<meta charset="utf-8">
<title>Winzerhof Dolmeck – Weinetikett</title>
<link rel="stylesheet" href="https://fonts.googleapis.com/css2?family=Montserrat:wght@300;400&display=swap">
<style>
  :root {
    --backdrop: #e6e4df;
    --label-paper: #f2efe6;
    --ink: #6f6a60;
    --olive: #a99b5c;
    --crimson: #9b2d55;
    --forest: #3e6a53;
    --saffron: #eab326;
  }
  html, body {
    margin: 0;
    padding: 0;
    width: 1200px;
    height: 1200px;
    overflow: hidden;
    background: var(--backdrop);
  }
  .canvas {
    width: 1200px;
    height: 1200px;
    display: flex;
    align-items: center;
    justify-content: center;
  }
  .wine-label {
    position: relative;
    width: 668px;
    height: 1080px;
    background: var(--label-paper);
    font-family: "Montserrat", sans-serif;
    color: var(--ink);
    box-shadow: 0 2px 10px rgba(0,0,0,0.08);
  }
  .brand-mark {
    position: absolute;
    top: 62px;
    left: 50%;
    width: 86px;
    height: 86px;
    margin-left: -43px;
    background: var(--forest);
  }
  .brand-name {
    position: absolute;
    top: 218px;
    left: 0;
    right: 0;
    text-align: center;
    font-size: 40px;
    font-weight: 400;
    letter-spacing: 0.32em;
    padding-left: 0.32em;
  }
  .brand-sub {
    position: absolute;
    top: 276px;
    left: 0;
    right: 0;
    text-align: center;
    font-size: 14px;
    font-weight: 400;
    letter-spacing: 0.42em;
    padding-left: 0.42em;
  }
  .label-artwork {
    position: absolute;
    top: 357px;
    left: 0;
    right: 0;
    height: 628px;
    background: linear-gradient(90deg,
      var(--olive) 0%,
      var(--olive) 14%,
      var(--crimson) 30%,
      var(--crimson) 40%,
      var(--forest) 55%,
      var(--forest) 72%,
      var(--saffron) 86%,
      var(--saffron) 100%);
    opacity: 0.85;
  }
  .volume {
    position: absolute;
    top: 1018px;
    left: 0;
    right: 0;
    text-align: center;
    font-size: 22px;
    font-weight: 400;
    letter-spacing: 0.2em;
    padding-left: 0.2em;
  }
</style>
</head>
<body>
  <main class="canvas">
    <section class="wine-label">
      <div class="brand-mark"></div>
      <h1 class="brand-name" style="margin:0">DOLMECK</h1>
      <p class="brand-sub" style="margin:0">WINZERHOF</p>
      <div class="label-artwork" role="img" aria-label="Grafik aus sich überlappenden, leicht geneigten Farbflächen in Oliv, Weinrot, Grün und Gelb"></div>
      <p class="volume" style="margin:0">0,75l</p>
    </section>
  </main>
</body>
</html>
```